Navelo Partnering Business Card

Hello everyone. We need a business card design that would match our logo and the theme we're trying to have for Navelo that you can find on our website and/or Corvapage page

```html
<!DOCTYPE html>
<html lang="en">
<head>
<meta charset="utf-8">
<title>Navelo Partnering Business Card</title>
<link rel="stylesheet" href="https://fonts.googleapis.com/css2?family=Open+Sans:wght@400;700&family=Arimo:wght@400;700&display=swap">
<style>
  :root {
    --backdrop: #2b2b2d;
    --card-white: #ffffff;
    --card-black: #121212;
    --brand-purple: #2e1b5e;
    --rule-grey: #cfcfcf;
    --divider-grey: #5a5a5a;
    --text-light: #f2f2f2;
    --text-muted: #d6d6d6;
    --social-a: #55acee;
    --social-b: #0a5c5a;
    --social-c: #2f6fb5;
  }
  * { box-sizing: border-box; margin: 0; padding: 0; }
  html, body { width: 1200px; height: 900px; overflow: hidden; }
  body {
    background: var(--backdrop);
    position: relative;
    font-family: "Arimo", Arial, sans-serif;
  }
  .card {
    position: absolute;
    left: 302px;
    width: 596px;
    height: 340px;
    overflow: hidden;
  }
  .card::after {
    content: "";
    position: absolute;
    left: 0; right: 0; bottom: 0;
    height: 8px;
    background: var(--brand-purple);
  }
  .card-front { top: 90px; background: var(--card-white); }
  .card-back { top: 470px; background: var(--card-black); }

  .brand {
    position: absolute;
    top: 98px;
    left: 0; right: 0;
    text-align: center;
    font-family: "Open Sans", sans-serif;
    font-weight: 700;
    font-size: 56px;
    line-height: 1;
    letter-spacing: -1px;
    color: var(--brand-purple);
  }
  .social-rule {
    position: absolute;
    top: 236px;
    left: 40px; right: 40px;
    display: flex;
    align-items: center;
    gap: 10px;
  }
  .social-rule .line { flex: 1; height: 1px; background: var(--rule-grey); }
  .social-links { display: flex; gap: 4px; }
  .social-link { width: 18px; height: 18px; border-radius: 2px; }
  .social-a { background: var(--social-a); }
  .social-b { background: var(--social-b); }
  .social-c { background: var(--social-c); }

  .identity {
    position: absolute;
    top: 110px;
    right: 340px;
    text-align: right;
    color: var(--text-light);
  }
  .person-name {
    font-family: "Open Sans", sans-serif;
    font-weight: 700;
    font-size: 19px;
    letter-spacing: 0.5px;
  }
  .person-role { font-size: 15px; color: var(--text-muted); margin-top: 2px; }
  .divider {
    position: absolute;
    left: 272px; top: 112px;
    width: 1px; height: 78px;
    background: var(--divider-grey);
  }
  .contacts {
    position: absolute;
    left: 292px; top: 108px;
    list-style: none;
    color: var(--text-light);
    font-size: 15px;
  }
  .contacts li { display: flex; align-items: center; gap: 8px; height: 21px; }
  .contacts svg { width: 12px; height: 12px; fill: var(--text-light); }
  .address {
    position: absolute;
    left: 60px; top: 250px;
    color: var(--text-light);
    font-size: 15px;
  }
</style>
</head>
<body>
  <section class="card card-front">
    <div class="brand">Navelo</div>
    <div class="social-rule">
      <span class="line"></span>
      <div class="social-links">
        <span class="social-link social-a" role="img" aria-label="Chirpline"></span>
        <span class="social-link social-b" role="img" aria-label="Xelora"></span>
        <span class="social-link social-c" role="img" aria-label="Corvapage"></span>
      </div>
      <span class="line"></span>
    </div>
  </section>

  <section class="card card-back">
    <div class="identity">
      <div class="person-name">DANIEL REEVE</div>
      <div class="person-role">Managing Director</div>
    </div>
    <span class="divider"></span>
    <ul class="contacts">
      <li><svg viewBox="0 0 12 12"><path d="M1 4c0-2 2-3 5-3s5 1 5 3v1H8V4H4v1H1z M3 6h6l2 5H1z"/></svg>044-555 018 274</li>
      <li><svg viewBox="0 0 12 12"><path d="M3 0h6v12H3z M4 1v9h4V1z" fill-rule="evenodd"/></svg>044-555 018 274</li>
      <li><svg viewBox="0 0 12 12"><path d="M0 2h12v8H0z M1 3l5 4 5-4z" fill-rule="evenodd"/></svg>info@navelo-mail.com</li>
      <li><svg viewBox="0 0 12 12"><circle cx="6" cy="6" r="6"/></svg>www.navelo-partners.com</li>
    </ul>
    <p class="address">12345, Address Goes Here Country Name, 123456.</p>
  </section>
</body>
</html>
```